依頼詳細
◇サイトマップ
①Home
②MENU&PRICE
③SALON INFO
④PRODUCTS
⑤COUPON
⑥GALLERY
⑦STAFF
⑧VOICE
⑨RECRUIT
⑩CONTACT
⑪BLOG(一覧)
⑫NEWS(一覧)
⑬CAT
⑭HAIR CARE

◇優先事項
1.ユーザビリティー
2.凝ったデザイン
3.編集更新

◇期待する効果
1.新規顧客の獲得
2.既存顧客の満足度向上
3.イメージアップ

◇ターゲット
【性別】男女比(男1 : 9女)
【年代】30代~40代
【属性】会社員 自営業 主婦

◇sns
Facebook 会社用

◇テイスト
◯シンプル ナチュラル かっこいい
×可愛い・キュート カラフル 高級感

※デザインのテイストとして僕自身の好みですが、ペンキの質感やコンクリートの質感が好きで、シンプルの中にかっこよさがあるデザインが好きです。
(少しでも参考にして頂ければ嬉しいです)

◇希望カラー
ベース色(ベージュ・白)
差し色 (茶系・緑系 アースカラー)
サイトURL
http://mizutama2047.com/
ページ数
1ページ
希望イメージ
シンプル 複雑
単色 カラフル
暗い 明るい
日常 高級
遊び心 厳粛
未来的 伝統的
女性的 男性的
希望する色
茶系、緑系、グレー系、ペースは白系で考えています。そのほかは茶色や緑が好きです。
納品ファイル
• イラストレーター形式 (.ai)
• フォトショップ形式 (.psd)
• PNG形式 (.png)
補足説明
素材①
撮影データをナギボックスドライブにアップしています。
下記URLよりダウンロードしてください。
http://nagibox.jp/download/c51e7a02d9b3f684e10a7c2bd5f93e8a61c04d77
ダウンロードパスワード pass

※素材として、コンクリートの写真があり、店内の打ちっぱなしの部分になりますが、上手く背景などで使えたらと思い写真を取りました、使えなさそうであれば無視して頂いても構いません。

素材➁
クレパド:https://jp.krepado.com/
当院で定期契約をしています。クレジット購入のみのもの以外をご利用下さい。
また定期契約のものは当院の負担となり、ランサー様に負担はありません。
カンプ画像を入れてください。
依頼公開後の追記内容
素材のダウンロードリンクが切れてしまっていたので再度アップロード致します。
ダウンロードをお願い致します。
http://nagibox.jp/download/9e4c1b7a35d0f28e6a17c9b4e02d5f3a8b76c1e9

ダウンロードパスワード pass

作成期間が少なくなってしまった人もいるので延長させていただきます。
もう少し提案が見たいため、延長させて頂きます。
■ 選んだ理由

デザインが良かったので選定致しました。

■ 提案者全員のお礼・コメント

皆様素敵なデザインをありがとうございました。

```html
<!DOCTYPE html>
<html lang="ja">
<head>
<meta charset="utf-8">
<title>HAIR SALON みずたま</title>
<link rel="stylesheet" href="https://fonts.googleapis.com/css2?family=Josefin+Sans:wght@400;600&family=Noto+Sans+JP:wght@400;500&display=swap">
<style>
:root{
  --bg:#ffffff;
  --ink:#222222;
  --muted:#9a9a9a;
  --accent:#8c7a2c;
  --line:#e2e2e2;
}
*{margin:0;padding:0;box-sizing:border-box}
html,body{width:1200px;height:2596px;overflow:hidden;background:var(--bg)}
body{position:relative;font-family:"Noto Sans JP",sans-serif;color:var(--ink)}
.abs{position:absolute}
.hero{left:96px;top:60px;width:1008px;height:508px;
  background:linear-gradient(120deg,#6e5a45 0%,#c9b39a 35%,#f1e8dc 55%,#b79c7c 80%,#5a4736 100%)}
.brand{left:132px;top:86px;color:#fff;display:flex;align-items:baseline;gap:14px;font-family:"Noto Sans JP",sans-serif;font-weight:500}
.brand small{font-size:14px;letter-spacing:2px}
.brand span{font-size:40px;letter-spacing:4px}
.tel{right:104px;top:66px;color:#fff;text-align:right;font-size:12px;line-height:1.3}
.tel strong{display:block;font-family:"Josefin Sans",sans-serif;font-size:26px;font-weight:600;letter-spacing:1px}
.gnav{left:96px;top:590px;width:1008px;display:flex;justify-content:space-between;
  font-family:"Josefin Sans",sans-serif;font-size:15px;font-weight:600;letter-spacing:1px;color:var(--ink)}
.photo{display:block}
.heading{font-family:"Josefin Sans",sans-serif;font-weight:600;font-size:29px;color:var(--accent);letter-spacing:1px}
.copy{font-size:14px;line-height:26px;color:var(--muted);letter-spacing:1px}
.p-news{left:224px;top:688px;width:336px;height:224px;background:linear-gradient(135deg,#e9dcc6,#b58d5c 60%,#6d5234)}
.p-blog{left:612px;top:904px;width:332px;height:224px;background:linear-gradient(135deg,#3b3028,#8a7560 50%,#d6c4a8)}
.p-concept{left:380px;top:1128px;width:332px;height:224px;background:radial-gradient(circle at 35% 40%,#f4dca0 0,#9c7038 25%,#1c1510 60%)}
.p-gallery{left:672px;top:1352px;width:336px;height:224px;background:linear-gradient(90deg,#f3e07a,#e8c958 50%,#f0dc74)}
.p-menu{left:232px;top:1568px;width:328px;height:224px;background:linear-gradient(160deg,#e8e6e2,#9b958c 55%,#4b463f)}
.p-staff{left:532px;top:1792px;width:332px;height:224px;background:linear-gradient(120deg,#2a2622,#8a7d70 55%,#e2dbd2)}
.p-products{left:328px;top:2012px;width:328px;height:220px;background:linear-gradient(180deg,#f1ede6,#c8bba6 60%,#8a7a66)}
.footer-brand{left:120px;top:2332px;display:flex;align-items:baseline;gap:12px;color:var(--accent);font-weight:500}
.footer-brand small{font-size:12px;letter-spacing:2px}
.footer-brand span{font-size:34px;letter-spacing:3px}
.address{left:120px;top:2412px;font-size:12px;line-height:18px;color:#555}
.fnav{left:0;top:2508px;width:1200px;display:flex;justify-content:center;gap:28px;font-size:12px;color:#666}
.copyright{left:0;top:2536px;width:1200px;text-align:center;font-size:11px;color:#777}
</style>
</head>
<body>
<header>
  <div class="abs hero photo" role="img" aria-label="Salon interior with white styling chairs and mirrors"></div>
  <div class="abs brand"><small>HAIR SALON</small><span>みずたま</span></div>
  <div class="abs tel">予約専用番号<strong>072-555-0148</strong></div>
  <nav class="abs gnav">
    <span>CONCEPT</span><span>MENU&amp;PRICE</span><span>SALON INFO</span><span>PRODUCTS</span><span>COUPON</span><span>GALLERY</span><span>STAFF</span><span>VOICE</span><span>CONTACT</span><span>CAT</span><span>HAIR CARE</span>
  </nav>
</header>

<main>
  <div class="abs photo p-news" role="img" aria-label="Pocket watch and wooden letter on a shelf"></div>
  <h2 class="abs heading" style="left:608px;top:708px">NEWS</h2>
  <p class="abs copy" style="left:608px;top:748px;width:520px">新しいお知らせはこちらに掲載いたします。営業日の変更や季節のキャンペーン情報などをご案内しております。ご来店前にぜひご確認ください。今月のおすすめメニューも更新中です。</p>

  <h2 class="abs heading" style="left:184px;top:944px">BLOG</h2>
  <p class="abs copy" style="left:184px;top:984px;width:420px">スタッフの日々の出来事やヘアケアのコツを綴っています。最新のスタイル紹介やサロンの様子もお届けしています。気軽にのぞいてみてください。</p>
  <div class="abs photo p-blog" role="img" aria-label="Warm pendant lights over the salon"></div>

  <div class="abs photo p-concept" role="img" aria-label="Glowing bulb lamp in dark interior"></div>
  <h2 class="abs heading" style="left:732px;top:1276px">CONCEPT</h2>

  <div class="abs photo p-gallery" role="img" aria-label="Hairstyle model against a yellow wall"></div>
  <h2 class="abs heading" style="left:532px;top:1496px">GALLERY</h2>

  <div class="abs photo p-menu" role="img" aria-label="Row of hair care bottles on a shelf"></div>
  <h2 class="abs heading" style="left:584px;top:1736px">MENU&amp;PRICE</h2>

  <div class="abs photo p-staff" role="img" aria-label="Stylist hands holding scissors"></div>
  <h2 class="abs heading" style="left:880px;top:1936px">STAFF</h2>

  <div class="abs photo p-products" role="img" aria-label="Hair products arranged on a white shelf"></div>
  <h2 class="abs heading" style="left:688px;top:2184px">PRODUCTS</h2>
</main>

<footer>
  <div class="abs footer-brand"><small>HAIR SALON</small><span>みずたま</span></div>
  <p class="abs address">伊丹市中央1丁目2番3号<br>予約専用番号　072-555-0148</p>
  <nav class="abs fnav"><span>SALON INFO</span><span>RECRUIT</span><span>CONTACT</span><span>プライバシーポリシー</span><span>サイトマップ</span></nav>
  <p class="abs copyright">Copyright © 2017 Mizutama All rights reserved.</p>
</footer>
</body>
</html>
```